Strata Edge Supply Business Card Design Challenge

Please create me a simple card using my logo. I'm not looking for anything abstract.
A couple of colours for text and maybe something on the card so the whole card isn't just a white board.
Please send me samples and I'll reply with suggestions to refine the design. Thank you

Reason: The Ormeau address was incorrect in the brief, so I have updated that so the 4 and 5 star submissions can be updated and resubmitted please!!! Sorry and thank you

Target Market(s)

Mining companies and rock producing aggregate companies. Quarries

Industry/Entity Type

Mining

Contact Information for Business Card

Name - Lewis Trenholm / Company Logo AND Strata Edge Supply Pty Ltd / position - Managing Director / address1 - Unit 3, 14 Kestrel Parade, Ormeau 4208 Queensland AU / address2 - PO Box 917, Oxenford 4210 Queensland AU / mobile - 0427 195 864 / phone - 07 5571 9346 / fax - 07 5571 9420 / email - lt@strataedgesupply.example.com.au / website - www.strataedgesupply.example.com.au

Requirements
Must have
• Business details as per the above. The phone and fax numbers will be confirmed before the end of the project. Thank you
• SINGLE SIDED ONLY please on Card, not transparent plastic

```html
<!DOCTYPE html>
<html lang="en">
<head>
<meta charset="utf-8">
<title>Strata Edge Supply – Business Card</title>
<link rel="stylesheet" href="https://fonts.googleapis.com/css2?family=Lato:wght@400;700&family=Saira:wght@400;600&display=swap">
<style>
  :root {
    --page: #3b3b3d;
    --paper-top: #ffffff;
    --paper-bottom: #eeeeef;
    --slate: #474b56;
    --blue: #1da0de;
    --ink: #3e4049;
    --light: #ffffff;
  }
  * { margin: 0; padding: 0; box-sizing: border-box; }
  html, body {
    width: 1200px; height: 750px; overflow: hidden;
    background: var(--page);
  }
  .card {
    position: absolute; left: 75px; top: 75px;
    width: 1050px; height: 600px;
    background: var(--slate);
    overflow: hidden;
  }
  .card__head {
    position: absolute; left: 0; top: 0;
    width: 100%; height: 297px;
    background: linear-gradient(to bottom, var(--paper-top), var(--paper-bottom));
  }
  .card__rule {
    position: absolute; left: 0; top: 297px;
    width: 100%; height: 5px;
    background: var(--blue);
  }
  .brand {
    position: absolute; left: 51px; top: 132px;
    display: flex; align-items: center; gap: 16px;
  }
  .brand__square { width: 38px; height: 38px; background: var(--blue); }
  .brand__name {
    font-family: "Lato", sans-serif; font-weight: 700;
    font-size: 38px; color: var(--ink); letter-spacing: 0.5px;
  }
  .person { position: absolute; left: 607px; top: 166px; }
  .person__name {
    font-family: "Saira", sans-serif; font-weight: 600;
    font-size: 37px; line-height: 1; color: var(--blue);
    text-transform: uppercase; letter-spacing: -0.3px;
  }
  .person__role {
    margin-top: 8px;
    font-family: "Saira", sans-serif; font-weight: 400;
    font-size: 27px; line-height: 1; color: var(--ink);
    text-transform: uppercase;
  }
  .contact {
    position: absolute; list-style: none;
    font-family: "Lato", sans-serif; font-size: 24px;
    color: var(--light);
  }
  .contact--left { left: 54px; top: 356px; }
  .contact--right { left: 600px; top: 358px; }
  .contact__item { display: flex; align-items: flex-start; gap: 14px; height: 40px; line-height: 36px; }
  .contact__item--address { height: 118px; }
  .contact__item--box { height: 78px; }
  .contact__icon { width: 27px; height: 36px; flex: none; }
  .contact__text { white-space: nowrap; }
  .contact__item--address .contact__text,
  .contact__item--box .contact__text { line-height: 38px; }
</style>
</head>
<body>
  <section class="card">
    <div class="card__head"></div>
    <div class="card__rule"></div>

    <div class="brand">
      <span class="brand__square"></span>
      <span class="brand__name">Strata Edge Supply</span>
    </div>

    <div class="person">
      <h1 class="person__name">Lewis Trenholm</h1>
      <p class="person__role">Managing Director</p>
    </div>

    <ul class="contact contact--left">
      <li class="contact__item">
        <svg class="contact__icon" viewBox="0 0 27 36" aria-hidden="true"><path fill="var(--blue)" d="M6 9c1.5-1.5 3-1 3.8.2l2.2 3.3c.6 1 .3 2-.5 2.7l-1.4 1.2c1.2 2.8 3.2 5 6 6.4l1.3-1.4c.8-.8 1.8-1 2.7-.3l3.2 2.3c1.1.8 1.3 2.3.1 3.6-1.7 1.9-4 2.5-6.7 1.2C9.6 25.2 5 19.6 4.5 14 4.3 11.8 4.8 10.2 6 9z"/></svg>
        <span class="contact__text">07 5571 9346</span>
      </li>
      <li class="contact__item">
        <svg class="contact__icon" viewBox="0 0 27 36" aria-hidden="true"><rect x="7" y="6" width="13" height="24" rx="2" fill="none" stroke="var(--blue)" stroke-width="2.6"/><circle cx="13.5" cy="26" r="1.4" fill="var(--blue)"/></svg>
        <span class="contact__text">0427 195 864</span>
      </li>
      <li class="contact__item">
        <svg class="contact__icon" viewBox="0 0 27 36" aria-hidden="true"><rect x="8" y="8" width="11" height="7" fill="var(--blue)"/><rect x="3" y="15" width="21" height="9" rx="2" fill="var(--blue)"/><rect x="7" y="22" width="13" height="6" fill="var(--blue)" stroke="var(--slate)" stroke-width="1.2"/></svg>
        <span class="contact__text">07 5571 9420</span>
      </li>
      <li class="contact__item">
        <svg class="contact__icon" viewBox="0 0 27 36" aria-hidden="true"><rect x="3" y="11" width="21" height="14" fill="var(--blue)"/><path d="M3 11l10.5 8L24 11" fill="none" stroke="var(--slate)" stroke-width="1.6"/></svg>
        <span class="contact__text">lt@strataedgesupply.example.com.au</span>
      </li>
      <li class="contact__item">
        <svg class="contact__icon" viewBox="0 0 27 36" aria-hidden="true"><circle cx="13.5" cy="18" r="9" fill="var(--blue)"/><path d="M9 13c2 1 2 3 4 3s1 3 3 4M15 10c0 2 2 3 4 3" fill="none" stroke="var(--slate)" stroke-width="1.4"/></svg>
        <span class="contact__text">strataedgesupply.example.com.au</span>
      </li>
    </ul>

    <ul class="contact contact--right">
      <li class="contact__item contact__item--address">
        <svg class="contact__icon" viewBox="0 0 27 36" aria-hidden="true"><path fill="var(--blue)" d="M13.5 4C8.3 4 5 7.8 5 12.5 5 19 13.5 30 13.5 30S22 19 22 12.5C22 7.8 18.7 4 13.5 4z"/><circle cx="13.5" cy="12.5" r="3.4" fill="var(--slate)"/></svg>
        <span class="contact__text">Strata Edge Supply Pty Ltd<br>Unit 3, 14 Kestrel Parade<br>Brackenvale 4291 Eastland AU</span>
      </li>
      <li class="contact__item contact__item--box">
        <svg class="contact__icon" viewBox="0 0 27 36" aria-hidden="true"><path d="M3 14h15v13H3zM18 14l6-4v13l-6 4M3 14l6-4h15" fill="none" stroke="var(--blue)" stroke-width="2"/><path d="M12 10V5h5v3h-3" fill="none" stroke="var(--blue)" stroke-width="2"/></svg>
        <span class="contact__text">PO Box 917<br>Tallow Creek 4293 Eastland AU</span>
      </li>
    </ul>
  </section>
</body>
</html>
```